Beauty Salon Industry - Web Design Project

zQuarta is a well-funded start up developing an Online Marketing Platform for small businesses in Europe.
We require a large number of high quality business web designs for our business website builder. Our business websites are seamlessly integrated into our Online Marketing systems and therefore it is important for designers to comply with our Design Guidelines.
This is our second contest and it will focus on the beauty salon industry. We will be running contents every 2-3 weeks for a new industry. Last month, we ran a contest for Builder website designs with 3 top prizes (plus £10 per variation) and we also paid out £25 per design for 20+ entries from designers who did not win the top prizes. So we encourage all entries!
We have included a wire frame this time to encourage you to be as creative as possible with your designs and layout while respecting the following guidelines:
1) You CAN change the layout as much as you like. If you think a vertical menu would look better, then use it. If you think the design would benefit from moving an element to a different location, then you can do that too.
2) You must include ALL the elements in the wire frame in your design.(e.g. latest 2 news entries, a testimonial, 1 gallery image, carousel etc...). Please make sure you have looked through the wire frame and know what is required. Entries that do not include all the elements will not qualify to win.
3) So remember, you CAN change the layout as much as you like but DO NOT remove any elements nor move them to a different page.
4) You may change the size and style of the carousel image. We would like to see as many variations of this as possible.
We are rewarding 3 prizes, and would like the winning designer to design the internal pages to the new design.
As always, if we think your designs could be incorporated into our system, but you do not win the competition, we will reward £25. Therefore, we encourage designers to submit as many designs as possible as we may award up to 25 designs.
Judging criteria : -
1) Visual Design
2) Layout must adhere to best practices and wireframe. If you decide to move elements around significantly please provide reason
3) Functional, informative and drives calls to action
Updates
As usual:
1st place = £350
2nd place = £250
3rd place = £150
Good luck!
Very happy with all the designs submitted so far, and will provide feedback ASAP.
We would like to see you try arranging the elements differently. So please try different navigation types and layouts.
Thanks
Morris
Prize funds for 1st place has been slightly increased.
Thanks
Morris
We have already had some amazing designs submitted. Thanks.
Remember to play with the layout of the elements and try designs with a carousel/slider that is in portrait not just in landscape.
Thanks everyone!
Morris
Hi everyone, we are really enjoying looking through the designs.
We have one NEW requirement. If you have used an image from http://www.frelik-example.com/ in your design, could you please replace it with another.
We are not associated with them.
Thank you.
I have just sent a poll around the office to vote on all the designs and hope to have the results soon.
Good luck and I hope to see all your great designs for our next project in a couple of weeks.
Morris
Hi everyone, we hope you have had a good holiday season. We will be rewarding the prizes very soon, hopefully today or tomorrow.
Thanks
Morris
We are currently going through all the designs that did not win our competition and will be contacting the designers of the designs we would like to use in our system, so please keep an eye on your inbox over the next few days.
Thank you
Morris
Target Market(s)
Beauty Salon Industry
Industry/Entity Type
Beauty Salon
Look and feel
Each slider illustrates characteristics of the customer's brand and the style your logo design should communicate.

```html
<!DOCTYPE html>
<html lang="en">
<head>
<meta charset="utf-8">
<title>Velvet Comb – Hair &amp; Urban Spa</title>
<link rel="stylesheet" href="https://fonts.googleapis.com/css2?family=Oswald:wght@300;400&family=Arimo:ital,wght@0,400;0,700;1,400&display=swap">
<style>
:root{
  --pink:#cf0a52;
  --pink-dark:#8e0437;
  --pink-light:#e63d78;
  --night:#141414;
  --night-2:#1d1d1d;
  --white:#ffffff;
  --ink:#222222;
  --muted:#333333;
  --teal:#2d4a4e;
  --head:"Oswald", "Arial Narrow", sans-serif;
  --body:"Arimo", Arial, sans-serif;
}
*{box-sizing:border-box;margin:0;padding:0}
html,body{width:1200px;height:990px;overflow:hidden}
body{position:relative;background:var(--white);font-family:var(--body);color:var(--white)}
.top{position:absolute;left:0;top:0;width:1200px;height:733px;
  background:var(--night);
  background-image:repeating-linear-gradient(45deg,rgba(255,255,255,.025) 0 1px,transparent 1px 3px),repeating-linear-gradient(-45deg,rgba(0,0,0,.25) 0 1px,transparent 1px 3px)}
.abs{position:absolute}

/* header */
.logo-box{left:148px;top:0;width:97px;height:68px;background:var(--white);color:#111;font-family:var(--head);font-weight:300;font-size:30px;display:flex;align-items:center;justify-content:center}
.brand{left:259px;top:14px;font-family:var(--body);font-weight:700;font-size:30px;color:var(--pink);letter-spacing:-.5px}
.tagline{left:259px;top:54px;font-style:italic;font-size:14px;color:var(--white)}
.phone{left:920px;top:8px;display:flex;align-items:center;gap:10px;font-size:15px}
.book-btn{left:955px;top:40px;width:96px;height:29px;background:var(--pink);font-size:15px;display:flex;align-items:center;justify-content:center}
.book-btn::before{content:"";position:absolute;left:-10px;top:0;border-top:10px solid var(--pink-dark);border-left:10px solid transparent}

/* nav */
.nav{left:141px;top:88px;width:918px;height:37px;background:linear-gradient(#d8155c,#c50848);display:flex;justify-content:space-between;align-items:center;padding:0 24px 0 20px;border-bottom:3px solid #f2f2f2;height:40px}
.nav a{font-family:var(--head);font-weight:300;font-size:19px;color:rgba(255,255,255,.72);text-decoration:none}
.nav a.current{color:rgba(255,255,255,.85)}
.nav-marker{left:163px;top:118px;width:0;height:0;border-left:12px solid transparent;border-right:12px solid transparent;border-bottom:10px solid var(--teal)}

/* panels */
.panel{background:var(--pink)}
.fold-r::after{content:"";position:absolute;right:-10px;top:0;border-top:10px solid var(--pink);border-right:10px solid transparent}
.fold-l::before{content:"";position:absolute;left:-10px;top:0;border-top:10px solid var(--pink);border-left:10px solid transparent}
.panel-title{font-family:var(--head);font-weight:300;font-size:19px;line-height:24px;padding-bottom:4px;border-bottom:1px solid rgba(255,255,255,.55);margin-bottom:8px}
.panel p{font-size:12px;line-height:19.6px}
.more{display:flex;justify-content:flex-end;align-items:center;gap:4px;font-style:italic;font-size:12px}
.panel .more{color:#3a0016}
.ph{background:linear-gradient(135deg,#5a5e66,#2c2f35)}

.intro{left:141px;top:162px;width:177px;height:331px;padding:6px 7px 0 8px}
.gallery{left:141px;top:518px;width:177px;height:200px;padding:10px 9px}
.gallery .ph{width:159px;height:152px;background:linear-gradient(135deg,#6c717a,#2b2e33)}
.gallery .more{margin-top:16px}

/* carousel */
.slide-side{top:183px;height:210px;background:linear-gradient(#e6e8eb,#c9ccd1)}
.slide-main{left:391px;top:162px;width:415px;height:257px;background:linear-gradient(120deg,#eef0f2,#d9c9bf 55%,#e7e9ec)}
.dots{left:548px;top:440px;display:flex;gap:4px}
.dots span{width:16px;height:16px;border-radius:50%;background:var(--white)}
.dots span.on{background:var(--pink)}

/* white cards */
.card{background:var(--white);color:var(--ink)}
.testimonial{left:338px;top:475px;width:523px;height:79px;padding:9px 12px 0 16px}
.testimonial p{font-style:italic;font-size:12px;line-height:20px}
.byline{text-align:right;color:var(--pink);font-style:italic;font-size:12px;margin-top:-2px}
.card .more{color:var(--pink);margin-top:8px}
.news{left:338px;top:572px;width:523px;height:146px;padding:8px 8px 0 16px}
.news-cols{display:flex;gap:40px}
.news-item{width:230px}
.news-item h3{font-family:var(--head);font-weight:300;font-size:19px;color:var(--pink);margin-bottom:4px}
.news-item p{font-style:italic;font-size:11.5px;line-height:19.6px}
.news-date{text-align:right;color:var(--pink);font-style:italic;font-size:11px;margin-top:4px}
.news .more{margin-top:0}

/* right column */
.offer{left:881px;top:162px;width:177px;height:230px;padding:10px 8px 0 11px}
.offer .ph{width:158px;height:102px;margin-left:0;background:linear-gradient(135deg,#f3f3f3,#c9a6ad 60%,#eee)}
.price{font-family:var(--head);font-weight:300;font-size:18px;margin-top:10px}
.offer p{margin-top:2px}
.offer-cta{font-family:var(--head);font-weight:300;font-size:18px;margin-top:6px}
.address{left:881px;top:414px;width:177px;height:126px;padding:8px 8px 0 10px}
.hours{left:881px;top:562px;width:177px;height:156px;padding:8px 8px 0 10px}
.hours p{line-height:19.6px}
.address .more{margin-top:14px}

/* brands */
.brand-card{top:747px;width:188px;height:147px;border:1px solid var(--pink);background:var(--white)}
.brand-card .ph{position:absolute;inset:8px}
.brand-band{top:893px;width:222px;height:35px;background:var(--pink);font-family:var(--head);font-weight:300;font-size:19px;display:flex;align-items:center;justify-content:center;color:#fff}
.brand-band::before,.brand-band::after{content:"";position:absolute;top:-10px;border-bottom:10px solid var(--pink-dark)}
.brand-band::before{left:0;border-left:16px solid transparent;border-right:0}
.brand-band::after{right:0;border-right:16px solid transparent}
.brand-shadow{top:928px;width:210px;height:14px;border-radius:50%;background:radial-gradient(ellipse at center top,rgba(0,0,0,.35),transparent 70%)}

/* footer */
.footer{left:837px;top:962px;font-family:var(--head);font-weight:300;font-size:17px;color:var(--ink);display:flex;gap:22px}
.base-line{left:0;top:988px;width:1200px;height:2px;background:#d6d6d6}
</style>
</head>
<body>
<div class="top"></div>

<header>
  <div class="abs logo-box">Logo</div>
  <div class="abs brand">Velvet Comb</div>
  <div class="abs tagline">Hair &amp; Urban Spa</div>
  <div class="abs phone">
    <svg width="20" height="26" viewBox="0 0 20 26" aria-hidden="true"><rect x="2" y="1" width="16" height="24" rx="3" fill="#9aa3ad"/><rect x="4.5" y="4" width="11" height="15" fill="#3f86c4"/><circle cx="10" cy="22" r="1.5" fill="#555"/></svg>
    <span>020 7946 0321</span>
  </div>
  <div class="abs book-btn">Book Now</div>
</header>

<nav class="abs nav">
  <a class="current" href="#">Home</a><a href="#">Services</a><a href="#">Gallery</a><a href="#">Testimonials</a><a href="#">News</a><a href="#">About Us</a><a href="#">Contact Us</a>
</nav>
<div class="abs nav-marker"></div>

<section class="abs panel intro fold-r">
  <h2 class="panel-title">Let Our Hair &amp; Beauty Skills Blow You Away</h2>
  <p>Velvet Comb is a passionate, creative team, dedicated to delivering a second to none, personal salon experience that will ‘blow’ your mind.</p>
  <p style="margin-top:19.6px">Where ultimate hairdressing comes hand-in-hand with style, glamour, fashion, inovation and skill to create an exquisite salon experience in the heart of London.</p>
  <div class="more" style="margin-top:6px">Read more... <svg width="12" height="14" viewBox="0 0 12 14"><path d="M2 1l7 6-7 6" fill="none" stroke="#fff" stroke-width="3"/></svg></div>
</section>

<section class="abs panel gallery fold-r">
  <div class="ph" role="img" aria-label="Gallery photo of a client having her hair washed at the salon"></div>
  <div class="more">View Gallery... <svg width="12" height="14" viewBox="0 0 12 14"><path d="M2 1l7 6-7 6" fill="none" stroke="#fff" stroke-width="3"/></svg></div>
</section>

<div class="abs slide-side" style="left:338px;width:53px" role="img" aria-label="Previous carousel slide"></div>
<div class="abs slide-side" style="left:806px;width:57px" role="img" aria-label="Next carousel slide"></div>
<div class="abs slide-main" role="img" aria-label="Carousel photo of a model holding a red lipstick"></div>
<div class="abs dots"><span class="on"></span><span></span><span></span><span></span></div>

<section class="abs card testimonial">
  <p>My hairstylist, Marisol, was truely amazing. She listened to exactly what I wanted, but also told me exactly what...</p>
  <div class="byline">Priya Dalton</div>
  <div class="more">Read more... <svg width="14" height="16" viewBox="0 0 14 16"><path d="M3 1l8 7-8 7" fill="none" stroke="#cf0a52" stroke-width="3"/></svg></div>
</section>

<section class="abs card news">
  <div class="news-cols">
    <article class="news-item">
      <h3>Book Now for Christmas</h3>
      <p>Our salon is very busy for the two weeks before Christmas, So please early.<br>Call 020 7946 0321, or contact us.</p>
      <div class="news-date">1Dec. 2011</div>
    </article>
    <article class="news-item">
      <h3>Want to be a Hair Model?</h3>
      <p>We always need models for our portfolio. If you want to become one please Contact us..</p>
      <div class="news-date" style="margin-top:23px">1Dec. 2011</div>
    </article>
  </div>
  <div class="more">More news... <svg width="14" height="16" viewBox="0 0 14 16"><path d="M3 1l8 7-8 7" fill="none" stroke="#cf0a52" stroke-width="3"/></svg></div>
</section>

<section class="abs panel offer">
  <div class="ph" role="img" aria-label="Photo of make-up products: lipsticks, brush and eyeshadow palette"></div>
  <div class="price">$ 25</div>
  <p>Complimentary gift for first-time clients!</p>
  <div class="offer-cta">Book Appointment Now</div>
</section>

<section class="abs panel address fold-l">
  <h2 class="panel-title">Velvet Address</h2>
  <p>12 Larkin Row, London<br>W2C 4QP</p>
  <div class="more">View Map... <svg width="12" height="14" viewBox="0 0 12 14"><path d="M2 1l7 6-7 6" fill="none" stroke="#fff" stroke-width="3"/></svg></div>
</section>

<section class="abs panel hours fold-l">
  <h2 class="panel-title">Business Hours</h2>
  <p>Mon. 9 am - 5 pm.<br>Tue. 9 am - 5 pm.<br>Wed. 9 am - 5 pm.<br>Thu. 9 am - 5 pm.<br>Fri. 9 am - 5 pm.<br>Sat. 9 am - 5 pm.</p>
</section>

<div class="abs brand-card" style="left:157px"><div class="ph" role="img" aria-label="Product photo of colourful hair styling bottles" style="background:linear-gradient(90deg,#b44fc0,#e85a9e,#f0a030,#f5d23a)"></div></div>
<div class="abs brand-card" style="left:389px"><div class="ph" role="img" aria-label="Product photo of white and purple hair care tubes" style="background:linear-gradient(135deg,#f1f1f4,#8a6bb0 55%,#eeeef2)"></div></div>
<div class="abs brand-card" style="left:621px"><div class="ph" role="img" aria-label="Product photo of assorted colourful hair care bottles" style="background:linear-gradient(135deg,#f6c2d8,#7fc6e6 45%,#f3e14d 75%,#f3f3f3)"></div></div>
<div class="abs brand-card" style="left:853px"><div class="ph" role="img" aria-label="Product photo of red hair styling products" style="background:linear-gradient(135deg,#f2f2f2,#c81e2b 50%,#f0f0f0)"></div></div>

<div class="abs brand-band" style="left:141px">Lumelle</div>
<div class="abs brand-band" style="left:373px">Norvana</div>
<div class="abs brand-band" style="left:605px">Brook ‘n’ bloom</div>
<div class="abs brand-band" style="left:837px">Kestrelle</div>
<div class="abs brand-shadow" style="left:147px"></div>
<div class="abs brand-shadow" style="left:379px"></div>
<div class="abs brand-shadow" style="left:611px"></div>
<div class="abs brand-shadow" style="left:843px"></div>

<footer class="abs footer"><span>Managed by zQuarta</span><span>Admin</span></footer>
<div class="abs base-line"></div>
</body>
</html>
```